Folded A4 flyer for design&construction company

Folded A4 flyer needed. Keywords: elegant, stylish
our website www.corvimo.ae

Industry/Entity Type

Construction

```html
<!DOCTYPE html>
<html lang="en">
<head>
<meta charset="utf-8">
<title>Corvimo – Design & Construction Flyer</title>
<link href="https://fonts.googleapis.com/css2?family=Archivo+Black&family=Sorts+Mill+Goudy&display=swap" rel="stylesheet">
<style>
  :root {
    --slate: #4a4a4b;
    --slate-light: #565657;
    --slate-dark: #3c3c3d;
    --gold: #c39a2e;
    --gold-text: #e4cf3c;
    --charcoal: #2b2b2b;
    --cream: #efe6d4;
  }
  html, body { margin: 0; padding: 0; overflow: hidden; }
  body { width: 1200px; height: 849px; background: var(--slate); }
  .flyer {
    position: relative; width: 1200px; height: 849px; overflow: hidden;
    background:
      repeating-linear-gradient(90deg, rgba(255,255,255,0.025) 0 2px, rgba(0,0,0,0.03) 2px 5px),
      linear-gradient(180deg, var(--slate-light), var(--slate) 50%, var(--slate-dark));
  }
  .photo { position: absolute; }
  .photo-foyer {
    left: 0; top: 0; width: 254px; height: 530px;
    background: linear-gradient(160deg, #f3e6c8 0%, #e8d6b3 45%, #cdb48c 75%, #efe7dc 100%);
    clip-path: polygon(0 0, 254px 0, 254px 328px, 84px 530px, 0 530px);
  }
  .photo-bath {
    left: 602px; top: 0; width: 274px; height: 296px;
    background: linear-gradient(135deg, #e9e2d2 0%, #cfc3ac 50%, #8d7c68 80%, #3a2e28 100%);
  }
  .photo-kitchen {
    left: 602px; top: 302px; width: 598px; height: 244px;
    background: linear-gradient(180deg, #d9d4cb 0%, #5a4f48 40%, #2a2320 65%, #d8cdb4 85%, #7a6d5e 100%);
  }
  .photo-waterfall {
    left: 340px; top: 364px; width: 260px; height: 485px;
    background: linear-gradient(180deg, #3f5a2c 0%, #6b7b4a 25%, #8c7a66 45%, #a99e90 60%, #6f5a48 75%, #4f6a35 100%);
    clip-path: polygon(104px 0, 260px 0, 260px 485px, 0 485px, 0 212px);
  }
  .photo-lounge {
    left: 918px; top: 549px; width: 282px; height: 300px;
    background: radial-gradient(circle at 70% 30%, #f4e7b8 0%, #c49a5e 35%, #8a6235 70%, #5a3c1f 100%);
  }
  .brand {
    position: absolute; left: 150px; top: 440px; width: 250px; text-align: center;
    font-family: "Sorts Mill Goudy", serif; font-size: 46px; color: var(--charcoal);
    letter-spacing: 1px;
  }
  .service-title {
    position: absolute; margin: 0;
    font-family: "Archivo Black", sans-serif; font-size: 26px; line-height: 1;
    color: var(--gold); letter-spacing: 0.5px;
  }
  .service-icon { position: absolute; width: 44px; height: 44px; }
  .service-list {
    position: absolute; margin: 0; padding: 0; list-style: none;
    font-family: "Sorts Mill Goudy", serif; font-size: 19px; line-height: 24px;
    color: var(--gold-text);
  }
  .service-list li { position: relative; padding-left: 17px; }
  .service-list li::before {
    content: ""; position: absolute; left: 0; top: 11px;
    width: 4px; height: 4px; border-radius: 50%; background: var(--gold-text);
  }
  .design-title { left: 320px; top: 52px; }
  .design-icon { left: 264px; top: 37px; }
  .design-list { left: 274px; top: 82px; }
  .fitout-title { left: 934px; top: 52px; }
  .fitout-icon { left: 884px; top: 36px; }
  .fitout-list { left: 896px; top: 81px; }
  .landscaping-title { left: 106px; top: 609px; }
  .landscaping-icon { left: 54px; top: 596px; }
  .landscaping-list { left: 64px; top: 645px; }
  .maintenance-title { left: 713px; top: 554px; }
  .maintenance-icon { left: 661px; top: 548px; }
  .maintenance-list { left: 672px; top: 595px; }
</style>
</head>
<body>
<main class="flyer">
  <div class="photo photo-foyer" role="img" aria-label="Photo of a luxury villa foyer with curved lit ceiling and staircase"></div>
  <div class="photo photo-bath" role="img" aria-label="Photo of a marble bathroom with glass shower"></div>
  <div class="photo photo-kitchen" role="img" aria-label="Photo of a modern kitchen with dark cabinets and stone counters"></div>
  <div class="photo photo-waterfall" role="img" aria-label="Photo of a landscaped garden with rock waterfall and flowers"></div>
  <div class="photo photo-lounge" role="img" aria-label="Photo of a curved wooden lounge interior with pendant lights"></div>

  <div class="brand">CORVIMO</div>

  <svg class="service-icon design-icon" viewBox="0 0 44 44" aria-hidden="true">
    <circle cx="22" cy="22" r="20" fill="none" stroke="#c39a2e" stroke-width="2.5"/>
    <rect x="12" y="14" width="18" height="16" fill="none" stroke="#c39a2e" stroke-width="2"/>
    <path d="M12 22h8v8M20 14v5" stroke="#c39a2e" stroke-width="2" fill="none"/>
    <path d="M27 18l8-10" stroke="#efe6d4" stroke-width="2.5"/>
  </svg>
  <h2 class="service-title design-title">DESIGN</h2>
  <ul class="service-list design-list">
    <li>Villas Interior Design</li>
    <li>Villas Exterior Design</li>
    <li>Landscape Design</li>
    <li>Retail Interior Design</li>
    <li>Office Interior Design</li>
    <li>Hospitality Interior Design</li>
    <li>Hotel Interior Design</li>
    <li>Hotel Exterior Design</li>
    <li>Restaurant Interior Design</li>
  </ul>

  <svg class="service-icon fitout-icon" viewBox="0 0 44 44" aria-hidden="true">
    <circle cx="22" cy="22" r="21" fill="#c39a2e"/>
    <path d="M12 22l10-9 10 9" fill="none" stroke="#fff" stroke-width="2.5"/>
    <rect x="15" y="21" width="14" height="10" fill="none" stroke="#fff" stroke-width="2.5"/>
  </svg>
  <h2 class="service-title fitout-title">FITOUT</h2>
  <ul class="service-list fitout-list">
    <li>Development Approvals</li>
    <li>Flooring Solutions</li>
    <li>Partition</li>
    <li>Sealing Solutions</li>
    <li>MEP Works</li>
    <li>Civil Works</li>
    <li>Joinery</li>
    <li>Glass and Aluminium<br>Works (subcontractor)</li>
  </ul>

  <svg class="service-icon landscaping-icon" viewBox="0 0 44 44" aria-hidden="true">
    <circle cx="22" cy="22" r="21" fill="#c39a2e"/>
    <path d="M10 34c2-8 3-12 6-16M16 34c1-7 2-11 6-18M22 34c0-6 2-12 8-16M28 34c1-5 3-8 7-10" stroke="#fff" stroke-width="2" fill="none"/>
  </svg>
  <h2 class="service-title landscaping-title">LANDSCAPING</h2>
  <ul class="service-list landscaping-list">
    <li>Soft Landscaping</li>
    <li>Irrigation Solutions</li>
    <li>Hard land Scaping</li>
    <li>External Lighting</li>
    <li>Swimming Pool &amp; Water<br>Features</li>
  </ul>

  <svg class="service-icon maintenance-icon" viewBox="0 0 44 44" aria-hidden="true">
    <circle cx="22" cy="22" r="21" fill="#c39a2e"/>
    <path d="M13 31l14-14M25 13l6 6" stroke="#fff" stroke-width="3" fill="none"/>
    <path d="M14 14l16 16" stroke="#fff" stroke-width="2.5"/>
  </svg>
  <h2 class="service-title maintenance-title">MAINTAINCE</h2>
  <ul class="service-list maintenance-list">
    <li>AC Repair</li>
    <li>Plumber Services</li>
    <li>Electric Repair</li>
    <li>Carpentry Work</li>
    <li>Gypsum Ceiling</li>
    <li>Painting Services</li>
    <li>Cleaning Services</li>
    <li>Emergency Services</li>
  </ul>
</main>
</body>
</html>
```